Pregnancy and Fertility Information Website

Hello Designers,
I need a website which provide tips and information about healthy and happy pregnancy. My website name is Lorvin medical.

The website should provide all the information needed throughout pregnancy and beyond ranging from pregnancy tracking tools and articles about common pregnancy concerns and what to expect during pregnancy,etc.
The details about first trimester, second trimester and third trimester should be highlighted in the website.

Top Navigation
Home, Fertility, Pregnancy basics, Articles, Tips and News

I'm looking for a simple and clean design which involves captivating images and colors but it shouldn't be crowded. The design must be professional and modern. An easy to navigate layout is a must.

Green, violet, blue and light yellow colors are my favorites but i'm open to other options.

Any questions. Kindly ask

Industry/Entity Type

Medical

```html
<!DOCTYPE html>
<html lang="en">
<head>
<meta charset="utf-8">
<title>Lorvin medical – A Happy &amp; Healthy Pregnancy</title>
<link href="https://fonts.googleapis.com/css2?family=Raleway:wght@400;500;600&family=Dancing+Script:wght@500&display=swap" rel="stylesheet">
<style>
  :root{
    --blue:#1f5fa8;
    --blue-deep:#18508f;
    --sky:#3f9fd0;
    --green:#62b34f;
    --green-soft:#a6d8a6;
    --yellow:#f6c400;
    --text:#4a4a4a;
    --line:#dde3ea;
    --grey-bg:#f1f2f4;
  }
  *{box-sizing:border-box;margin:0;padding:0}
  html,body{width:1200px;height:4369px;overflow:hidden}
  body{font-family:"Raleway",Arial,sans-serif;color:var(--text);background:#fff;position:relative}
  h1,h2,h3,h4{font-weight:400}
  .abs{position:absolute}
  a{color:inherit;text-decoration:none}

  /* header + hero */
  .hero{left:0;top:0;width:1200px;height:760px;background:linear-gradient(180deg,#fff 0%,#f4f5f7 100%);overflow:hidden}
  .brand{left:80px;top:26px;display:flex;align-items:center;gap:10px;font-size:20px;font-weight:600;color:var(--blue)}
  .brand-dot{width:34px;height:34px;border-radius:50%;background:var(--green)}
  .nav{left:512px;top:38px;display:flex;gap:22px;font-size:15px;color:var(--blue)}
  .nav a.active{color:var(--green)}
  .hero-photo{left:700px;top:0;width:500px;height:720px;background:linear-gradient(180deg,#f1ece8 0%,#ece0d4 40%,#f3d77a 75%,#f2cd4a 100%)}
  .hero-title{left:80px;top:206px;font-size:50px;line-height:58px;color:var(--blue)}
  .hero-title .g{color:var(--green)}
  .hero-text{left:80px;top:342px;width:570px;font-size:15px;line-height:25px;color:#555}
  .btn{display:flex;align-items:center;justify-content:center;gap:10px;background:var(--yellow);color:#333;font-size:14px;font-weight:500;width:240px;height:42px}
  .hero-btn{left:82px;top:446px}
  .hero-curve{left:0;top:600px;width:1200px;height:170px}
  .hero-badge{left:560px;top:682px;width:80px;height:80px;border-radius:50%;background:#fff;border:3px solid var(--yellow)}
  .hero-badge::after{content:"";position:absolute;left:14px;top:14px;width:46px;height:46px;border-radius:50%;background:var(--green)}

  /* section headings */
  .sec-title{left:0;width:1200px;text-align:center;font-size:35px;color:var(--blue)}
  .sec-sub{left:0;width:1200px;text-align:center;font-family:"Dancing Script",cursive;font-size:19px;color:var(--green)}
  .sec-sub span::before,.sec-sub span::after{content:"";display:inline-block;width:24px;height:1px;background:var(--green);vertical-align:middle;margin:0 10px}

  /* care grid */
  .care-card{width:332px;height:218px;overflow:hidden}
  .care-img{width:100%;height:178px}
  .care-label{height:40px;background:var(--green);color:#fff;font-size:15px;text-align:center;line-height:40px}

  /* calculator */
  .calc{left:0;top:1486px;width:1200px;height:548px;background:linear-gradient(90deg,#eef0f3 0%,#f3f3f4 45%,#e4dcd3 70%,#d9d2cb 100%)}
  .calc-title{left:80px;top:1582px;font-size:42px;color:var(--blue)}
  .calc-text{left:80px;top:1660px;width:520px;font-size:13.5px;line-height:24px;color:#555}
  .calc-btn{left:82px;top:1823px}
  .calc-circle{left:862px;top:1700px;width:186px;height:186px;border-radius:50%;background:#fff;box-shadow:0 4px 16px rgba(0,0,0,.15)}
  .calc-circle div{position:absolute;left:38px;top:40px;width:110px;height:106px;background:linear-gradient(180deg,#d8262e 0 22%,#f4f4f4 22%)}

  /* journey */
  .tabs{left:79px;top:2214px;width:1041px;height:134px;display:flex;border:1px solid var(--line)}
  .tab{flex:1;border-left:1px solid var(--line);display:flex;flex-direction:column;align-items:center;justify-content:center;gap:14px;font-size:14px;color:#8fb4d6}
  .tab:first-child{border:2px solid var(--blue);color:var(--blue)}
  .tab i{width:44px;height:44px;border-radius:50%;display:block}
  .j-title{left:80px;top:2404px;font-size:21px;color:var(--blue);border-bottom:1px solid var(--blue);padding-bottom:4px}
  .j-text{left:80px;top:2464px;width:580px;font-size:13px;line-height:22px;color:#666}
  .j-text p{margin-bottom:18px}
  .j-text b{color:#333;font-weight:600}
  .j-img{left:760px;top:2420px;width:210px;height:210px;border-radius:50%;background:linear-gradient(160deg,#f1e9e2,#b9d3e6 55%,#f3f3f3)}

  /* trimester */
  .tri{left:0;top:2811px;width:1200px;height:1165px;background:var(--grey-bg)}
  .figure{width:200px;height:395px;background:linear-gradient(180deg,#e9ebee,#dfe6e5)}
  .col{width:241px}
  .col-head{height:38px;color:#fff;font-size:17px;line-height:38px;text-align:center}
  .col-body{background:#fff;height:442px;padding:18px 14px 0;border-bottom:5px solid}
  .row{display:flex;align-items:center;gap:12px;height:103px}
  .row.rev{flex-direction:row-reverse}
  .ico{flex:0 0 60px;height:60px;border-radius:50%;display:flex;align-items:center;justify-content:center}
  .row p{font-size:12.5px;line-height:19px;color:#777}

  /* footer */
  .footer{left:0;top:3976px;width:1200px;height:347px;background:linear-gradient(90deg,var(--blue-deep),#2470b8)}
  .f-col{top:4026px;color:#fff}
  .f-col h4{font-size:19px;margin-bottom:18px}
  .f-col ul{list-style:none;font-size:13px;line-height:25px}
  .f-col ul li::before{content:"› ";}
  .f-contact p{font-size:13px;line-height:20px;display:flex;gap:10px;margin-bottom:10px}
  .f-news p{font-size:12px;line-height:18px;width:230px;margin-bottom:12px}
  .f-input{width:210px;height:26px;background:#fff;color:#999;font-size:11px;padding:6px}
  .f-sub{margin-top:10px;width:70px;height:22px;background:var(--yellow);color:#333;font-size:11px;text-align:center;line-height:22px}
  .f-social li{display:flex;align-items:center;gap:10px;margin-bottom:8px;font-size:13px}
  .f-social li::before{content:none}
  .f-social i{width:20px;height:20px;background:rgba(255,255,255,.85);display:block}
  .bottom{left:0;top:4323px;width:1200px;height:46px;background:var(--green);color:#fff;font-size:11px}
  .bottom .l{position:absolute;left:80px;top:16px}
  .bottom .r{position:absolute;right:80px;top:16px;display:flex;gap:30px}
</style>
</head>
<body>

<section class="hero abs">
  <div class="hero-photo abs" role="img" aria-label="Photo: smiling expectant mother in a yellow top holding her belly"></div>
</section>
<div class="brand abs"><span class="brand-dot"></span>Lorvin medical</div>
<nav class="nav abs">
  <a class="active">Home</a><a>About Us</a><a>Fertility</a><a>Pregnancy Basics</a><a>Articles</a><a>Tips &amp; News</a><a>Contacts</a>
</nav>
<h1 class="hero-title abs"><span class="g">A</span> Happy &amp; Healthy<br>Pregnancy <span class="g">Is In Your</span> Hands</h1>
<p class="hero-text abs">Lorem ipsum dolor sit amet, consectetur adipiscing elit. Vivamus at iaculis enim. Pellentesque eget consequat nulla. Praesent semper turpis sed neque malesuada dignissim.</p>
<a class="btn hero-btn abs">Learn More <span>⟶</span></a>
<svg class="hero-curve abs" viewBox="0 0 1200 170" preserveAspectRatio="none">
  <path d="M0 20 Q600 210 1200 20 L1200 170 L0 170 Z" fill="#fff"/>
  <path d="M0 20 Q600 210 1200 20" fill="none" stroke="#f6c400" stroke-width="3"/>
</svg>
<div class="hero-badge abs"></div>

<h2 class="sec-title abs" style="top:820px">We Care For You</h2>
<div class="sec-sub abs" style="top:868px"><span>Learn The Facts</span></div>

<div class="care-card abs" style="left:79px;top:938px"><div class="care-img" role="img" aria-label="Photo: microscope view of an egg cell" style="background:linear-gradient(135deg,#1b6fb0,#7cc3e8,#e37a3c)"></div><div class="care-label">Understand Ovulation</div></div>
<div class="care-card abs" style="left:434px;top:938px"><div class="care-img" role="img" aria-label="Photo: woman feeling morning sickness" style="background:linear-gradient(135deg,#f7f2ee,#eeb8c8)"></div><div class="care-label">Pregnancy Symptoms</div></div>
<div class="care-card abs" style="left:789px;top:938px"><div class="care-img" role="img" aria-label="Photo: pregnant women exercising on fitness balls" style="background:linear-gradient(135deg,#e8ecef,#5f8ec6,#e6e0d7)"></div><div class="care-label">Exercise During Pregnancy</div></div>
<div class="care-card abs" style="left:79px;top:1186px"><div class="care-img" role="img" aria-label="Photo: pregnant belly with vitamins and fruit" style="background:linear-gradient(135deg,#f4ece6,#f0c9b4)"></div><div class="care-label">Prenatal Vitamins</div></div>
<div class="care-card abs" style="left:434px;top:1186px"><div class="care-img" role="img" aria-label="Photo: mother with her baby" style="background:linear-gradient(135deg,#f6e3d6,#d9b39a)"></div><div class="care-label">Maternal Care</div></div>
<div class="care-card abs" style="left:789px;top:1186px"><div class="care-img" role="img" aria-label="Photo: pregnant woman resting in bed" style="background:linear-gradient(135deg,#eef0f4,#c9cfd9)"></div><div class="care-label">High Risk Pregnancy Care</div></div>

<section class="calc abs" role="img" aria-label="Photo: happy woman looking at a pregnancy test"></section>
<h2 class="calc-title abs">Pregnancy Calculator</h2>
<p class="calc-text abs">Lorem ipsum dolor sit amet, consectetur adipiscing elit. Mauris eget dapibus nibh. Sed aliquam nibh magna, a bibendum nunc laoreet et. Ut accumsan leo massa, id rutrum turpis bibendum ut. Nulla eu augue eget nulla vehicula molestie. In fringilla ullamcorper ante, in placerat urna ultricies non. In venenatis ipsum nunc. Duis et accumsan lectus.</p>
<a class="btn calc-btn abs">Calculate Yours <span>⟶</span></a>
<div class="calc-circle abs" role="img" aria-label="Calendar page marking a due date"><div></div></div>

<h2 class="sec-title abs" style="top:2088px">The Journey Of Joy</h2>
<div class="sec-sub abs" style="top:2136px"><span>Plan Table</span></div>
<div class="tabs abs">
  <div class="tab"><i style="background:#2d7cc4"></i>Getting Pregnant</div>
  <div class="tab"><i style="background:#7bc36a"></i>Pregnancy</div>
  <div class="tab"><i style="background:#5aa86a"></i>Your First Scan</div>
  <div class="tab"><i style="background:#8cc56f"></i>Baby Birth</div>
  <div class="tab"><i style="background:#4e95d0"></i>Baby Care</div>
  <div class="tab"><i style="background:#7fc06c"></i>Baby Feeding</div>
</div>
<h3 class="j-title abs">Getting Pregnant</h3>
<div class="j-text abs">
  <p>Etiam eu libero efficitur euismod nibh sed, interdum ipsum. Maecenas lobortis magna at odio imperdiet auctor. Fusce sodales iaculis ante, nec tristique libero. Fusce sed est felis. Phasellus molestie varius rhoncus.</p>
  <p>Nam sapien quam, consectetur ut est vitae, auctor rutrum lorem. Nunc sit amet ipsum et ligula malesuada bibendum. In ligula velit, tristique sit amet fringilla sit amet, eleifend id leo. Sed egestas arcu a arcu tristique egestas.</p>
  <p><b>Note:</b> Fusce commodo imperdiet lacus. Proin et tortor bibendum, luctus urna ac, pellentesque. Praesent at enim at nulla dignissim sagittis pellentesque non nulla.</p>
</div>
<div class="j-img abs" role="img" aria-label="Photo: expectant mother in a kitchen with fresh vegetables"></div>

<section class="tri abs"></section>
<h2 class="sec-title abs" style="top:2870px">Pregnancy Trimester Chart</h2>
<div class="sec-sub abs" style="top:2918px"><span>All Stages</span></div>

<div class="figure abs" style="left:99px;top:3000px" role="img" aria-label="Illustration: woman in early pregnancy"></div>
<div class="figure abs" style="left:367px;top:3000px" role="img" aria-label="Illustration: woman in mid pregnancy"></div>
<div class="figure abs" style="left:635px;top:3000px" role="img" aria-label="Illustration: woman in late pregnancy"></div>
<div class="figure abs" style="left:903px;top:3000px" role="img" aria-label="Illustration: mother holding her newborn"></div>

<div class="col abs" style="left:79px;top:3423px">
  <div class="col-head" style="background:var(--blue)">1. Trimester</div>
  <div class="col-body" style="border-color:var(--blue)">
    <div class="row"><span class="ico" style="background:var(--blue)"><svg width="28" height="28"><rect x="4" y="6" width="20" height="18" fill="none" stroke="#fff" stroke-width="2"/><line x1="4" y1="11" x2="24" y2="11" stroke="#fff" stroke-width="2"/></svg></span><p>Nulla ultrices nisi nisi, mollis interdum ante finibus sit amet.</p></div>
    <div class="row rev"><span class="ico" style="background:var(--blue)"><svg width="28" height="28"><path d="M7 4h14L14 14l7 10H7l7-10z" fill="none" stroke="#fff" stroke-width="2"/></svg></span><p>Nulla ultrices nisi nisi, mollis interdum ante finibus sit amet.</p></div>
    <div class="row"><span class="ico" style="background:var(--blue)"><svg width="28" height="28"><line x1="5" y1="23" x2="23" y2="5" stroke="#fff" stroke-width="4"/></svg></span><p>Nulla ultrices nisi nisi, mollis interdum ante finibus sit amet.</p></div>
    <div class="row rev"><span class="ico" style="background:var(--blue)"><svg width="28" height="28"><circle cx="14" cy="14" r="9" fill="none" stroke="#fff" stroke-width="2"/></svg></span><p>Nulla ultrices nisi nisi, mollis interdum ante finibus sit amet.</p></div>
  </div>
</div>
<div class="col abs" style="left:347px;top:3423px">
  <div class="col-head" style="background:var(--green)">2. Trimester</div>
  <div class="col-body" style="border-color:var(--green)">
    <div class="row"><span class="ico" style="background:var(--green)"><svg width="28" height="28"><circle cx="14" cy="15" r="9" fill="#fff"/></svg></span><p>Nulla ultrices nisi nisi, mollis interdum ante finibus sit amet.</p></div>
    <div class="row rev"><span class="ico" style="background:var(--green)"><svg width="28" height="28"><circle cx="14" cy="14" r="10" fill="none" stroke="#fff" stroke-width="2"/><circle cx="14" cy="14" r="3" fill="#fff"/></svg></span><p>Nulla ultrices nisi nisi, mollis interdum ante finibus sit amet.</p></div>
    <div class="row"><span class="ico" style="background:var(--green)"><svg width="28" height="28"><rect x="4" y="8" width="20" height="14" fill="none" stroke="#fff" stroke-width="2"/><circle cx="14" cy="15" r="4" fill="#fff"/></svg></span><p>Nulla ultrices nisi nisi, mollis interdum ante finibus sit amet.</p></div>
    <div class="row rev"><span class="ico" style="background:var(--green)"><svg width="28" height="28"><path d="M14 23 4 13a5 5 0 0 1 10-6 5 5 0 0 1 10 6z" fill="#fff"/></svg></span><p>Nulla ultrices nisi nisi, mollis interdum ante finibus sit amet.</p></div>
  </div>
</div>
<div class="col abs" style="left:615px;top:3423px">
  <div class="col-head" style="background:var(--sky)">3. Trimester</div>
  <div class="col-body" style="border-color:var(--sky)">
    <div class="row"><span class="ico" style="background:var(--sky)"><svg width="28" height="28"><circle cx="14" cy="14" r="9" fill="none" stroke="#fff" stroke-width="2"/></svg></span><p>Nulla ultrices nisi nisi, mollis interdum ante finibus sit amet.</p></div>
    <div class="row rev"><span class="ico" style="background:var(--sky)"><svg width="28" height="28"><rect x="11" y="3" width="6" height="22" rx="3" fill="#fff" transform="rotate(45 14 14)"/></svg></span><p>Nulla ultrices nisi nisi, mollis interdum ante finibus sit amet.</p></div>
    <div class="row"><span class="ico" style="background:var(--sky)"><svg width="28" height="28"><circle cx="14" cy="10" r="5" fill="#fff"/><rect x="7" y="16" width="14" height="8" rx="4" fill="#fff"/></svg></span><p>Nulla ultrices nisi nisi, mollis interdum ante finibus sit amet.</p></div>
    <div class="row rev"><span class="ico" style="background:var(--sky)"><svg width="28" height="28"><line x1="5" y1="23" x2="23" y2="5" stroke="#fff" stroke-width="4"/></svg></span><p>Nulla ultrices nisi nisi, mollis interdum ante finibus sit amet.</p></div>
  </div>
</div>
<div class="col abs" style="left:883px;top:3423px">
  <div class="col-head" style="background:var(--green-soft)">Baby Birth</div>
  <div class="col-body" style="border-color:var(--green-soft)">
    <div class="row"><span class="ico" style="background:var(--green-soft)"><svg width="28" height="28"><circle cx="14" cy="9" r="5" fill="#fff"/><rect x="8" y="15" width="12" height="9" rx="4" fill="#fff"/></svg></span><p>Nulla ultrices nisi nisi, mollis interdum ante finibus sit amet.</p></div>
    <div class="row rev"><span class="ico" style="background:var(--green-soft)"><svg width="28" height="28"><ellipse cx="11" cy="16" rx="5" ry="8" fill="#fff"/><ellipse cx="19" cy="12" rx="3" ry="5" fill="#fff"/></svg></span><p>Nulla ultrices nisi nisi, mollis interdum ante finibus sit amet.</p></div>
    <div class="row"><span class="ico" style="background:var(--green-soft)"><svg width="28" height="28"><rect x="4" y="10" width="20" height="10" rx="5" fill="#fff"/></svg></span><p>Nulla ultrices nisi nisi, mollis interdum ante finibus sit amet.</p></div>
    <div class="row rev"><span class="ico" style="background:var(--green-soft)"><svg width="28" height="28"><rect x="9" y="8" width="10" height="17" rx="3" fill="#fff"/><rect x="12" y="3" width="4" height="5" fill="#fff"/></svg></span><p>Nulla ultrices nisi nisi, mollis interdum ante finibus sit amet.</p></div>
  </div>
</div>

<footer class="footer abs"></footer>
<div class="f-col abs" style="left:79px">
  <h4>Quick Links</h4>
  <ul><li>Home</li><li>About Us</li><li>Fertility</li><li>Pregnancy Basics</li><li>Articles</li><li>Tips &amp; News</li><li>Contacts</li></ul>
</div>
<div class="f-col f-contact abs" style="left:303px;width:300px">
  <h4>Contact Information</h4>
  <p><svg width="12" height="16"><path d="M6 15C2 9 1 7 1 5a5 5 0 0 1 10 0c0 2-1 4-5 10z" fill="#fff"/></svg><span>ABN 00 000 000 Head Office: 14 Alder Lane, Harbour Park, Eastvale 3120<br>PO Box 1180, Eastvale DC 3121</span></p>
  <p><svg width="12" height="16"><rect x="2" y="2" width="8" height="12" rx="2" fill="#fff"/></svg><span>Freecall: 1800 555 0147</span></p>
  <p><svg width="12" height="16"><rect x="0" y="4" width="12" height="8" fill="#fff"/></svg><span>info@lorvinmedical.example</span></p>
</div>
<div class="f-col f-news abs" style="left:641px">
  <h4>Newsletter Signup</h4>
  <p>Please enter your email address below to recieve our FREE newsletter</p>
  <div class="f-input">Your Email ID</div>
  <div class="f-sub">Subscribe</div>
</div>
<div class="f-col abs" style="left:932px">
  <h4>Follow Us</h4>
  <ul class="f-social"><li><i></i>Community</li><li><i></i>Network</li><li><i></i>Updates</li><li><i></i>Email</li></ul>
</div>
<div class="bottom abs">
  <span class="l">Copyright Lorvin medical. All Rights Are Reserved</span>
  <span class="r"><span>Join Us</span><span>Login to Lorvin Online</span><span>Support</span></span>
</div>

</body>
</html>
```